13 Tavo - new website design project

Our company Tavo Electrical is developing a new lead generation website focused on Electrical, LED Lighting and Solar Power. We need a high converting website.

Example of our current website is www.tavoelectrical.com.au You can take content from this website for this new design. Our colours are red, black and white. For our new website we would like to promote Tavo, Bright Days Ahead. Please listen to the jingle.

The below link is the company jingle that we have developed.
http://www.tunecraftaudio.com.au/tav-tc-v1/

The key for this brief is to generate leads for Electrical, LED Lighting (for commercial) and Solar Power & Storage.

Target Market(s)

Business owners in Melbourne Victoria

Number of Pages Required

4 page

Colors
ec1f27
ffffff

Requirements
Must have
• This page must be clean, be in line with company branding and a high converting lead website.

```html
<!DOCTYPE html>
<html lang="en">
<head>
<meta charset="utf-8">
<title>Tavo Electrical</title>
<link href="https://fonts.googleapis.com/css2?family=Roboto:wght@300;400;500;700&family=Roboto+Condensed:wght@400;700&display=swap" rel="stylesheet">
<style>
:root{
  --red:#ec1f27;
  --white:#ffffff;
  --ink:#333333;
  --muted:#555555;
  --band:#262626;
  --base:#111111;
  --grey:#e1e1e1;
  --numbox:#d9d9d9;
}
*{box-sizing:border-box;margin:0;padding:0}
html,body{width:1200px;height:2525px;overflow:hidden}
body{position:relative;font-family:'Roboto',sans-serif;color:var(--ink);background:var(--white)}
.abs{position:absolute}

/* hero */
.hero{left:0;top:0;width:1200px;height:586px;background:linear-gradient(135deg,#5b5f66 0%,#2e3a52 35%,#1e2c48 55%,#6a5a4c 80%,#8a7a6a 100%)}
.hero-shade{left:0;top:0;width:1200px;height:586px;background:rgba(0,0,0,.35)}
.social{top:4px;display:flex;gap:8px;left:160px}
.social span{width:19px;height:19px;border-radius:50%;background:var(--red);display:block}
.phone{left:887px;top:0;width:151px;height:34px;background:var(--white);display:flex;align-items:center;gap:8px;padding-left:12px;font-weight:700;color:var(--red);font-size:17px}
.phone .ic{width:22px;height:22px;border-radius:50%;background:var(--red);display:flex;align-items:center;justify-content:center}
.phone .brand{color:var(--ink);font-size:15px}
.nav{left:160px;top:34px;width:878px;height:72px;background:var(--red)}
.logo{left:0;top:0;width:121px;height:72px;background:var(--white);display:flex;align-items:center;justify-content:center;font-family:'Roboto Condensed',sans-serif;font-weight:700;font-size:30px;color:var(--red)}
.menu{right:0;top:0;height:72px;display:flex;font-size:10.5px;font-weight:500;color:var(--white)}
.menu a{display:flex;align-items:center;padding:0 11px;text-decoration:none;color:inherit}
.menu a.active{background:var(--white);color:var(--red);padding:0 12px}
.hero-title{left:0;width:1200px;top:272px;text-align:center;font-family:'Roboto Condensed',sans-serif;font-weight:700;font-size:33px;color:var(--white);letter-spacing:.5px}
.hero-title i{font-style:normal;color:var(--red);font-size:22px;margin:0 12px;vertical-align:3px}
.hero-sub{left:0;width:1200px;top:322px;text-align:center;font-size:14px;color:var(--white);letter-spacing:.5px}
.btn{background:var(--red);color:var(--white);font-size:11px;font-weight:500;display:flex;align-items:center;justify-content:center;gap:12px}
.hero-btn{left:534px;top:374px;width:134px;height:35px}
.services{left:0;top:586px;width:1200px;height:122px;background:var(--band)}
.svc{width:200px;text-align:center;color:var(--white);font-size:14px}
.svc .circle{width:124px;height:124px;border-radius:50%;background:var(--red);border:5px solid var(--white);margin:0 auto 14px;display:flex;align-items:center;justify-content:center}

/* about */
.about-frame{left:175px;top:769px;width:350px;height:234px;border:6px solid #111}
.about-photo{left:205px;top:799px;width:352px;height:234px;background:linear-gradient(120deg,#c98a60,#e6b48e 45%,#8a5a3c)}
.h2{font-family:'Roboto Condensed',sans-serif;font-size:21px;color:var(--ink);font-weight:400}
.h2 b{color:var(--red);font-weight:700}
.about-h{left:589px;top:798px}
.about-p{left:589px;top:846px;width:450px;font-size:11.5px;line-height:21px;color:var(--muted)}
.about-btn{left:589px;top:947px;width:88px;height:31px;font-size:10.5px}

/* section headings */
.sec-head{left:0;width:1200px;text-align:center}
.sec-head .rule{width:56px;height:2px;background:var(--red);margin:9px auto 0}

/* reasons */
.reason{width:290px}
.reason .num{left:0;top:0;width:37px;height:37px;background:var(--numbox);display:flex;align-items:center;justify-content:center;font-style:italic;font-size:17px;color:var(--ink)}
.reason h3{position:absolute;left:54px;top:-2px;font-family:'Roboto Condensed',sans-serif;font-size:13.5px;font-weight:700;color:var(--ink);white-space:nowrap}
.reason p{position:absolute;left:54px;top:22px;width:232px;font-size:11px;line-height:20px;color:var(--muted)}

/* testimonial */
.testi{left:0;top:1619px;width:1200px;height:266px;background:var(--grey)}
.avatar{left:248px;top:1640px;width:156px;height:156px;border-radius:50%;border:5px solid var(--white);background:linear-gradient(180deg,#dfe6ee 0%,#9aa6b3 40%,#5d6772 100%)}
.quote-mark{left:436px;top:1672px;font-family:Georgia,serif;font-size:70px;line-height:1;color:#9a9a9a}
.quote{left:505px;top:1674px;width:470px;font-size:11.5px;line-height:20px;color:var(--muted);text-transform:uppercase;letter-spacing:.3px}
.author{left:505px;top:1741px;font-size:10.5px;color:var(--muted)}
.author em{font-size:9px;color:#888}
.arrows{left:572px;top:1843px;display:flex;gap:2px}
.arrows span,.carr{width:28px;height:27px;background:#333;display:flex;align-items:center;justify-content:center}

/* clients */
.client{top:2040px;height:94px;display:flex;align-items:center;justify-content:center;background:var(--white);border:1px solid #ddd;font-family:'Roboto Condensed',sans-serif;font-weight:700;font-size:20px;color:var(--ink)}
.carr{top:2077px;width:19px;height:20px}

/* footer */
.footer{left:0;top:2178px;width:1200px;height:274px;background:var(--band);color:#bbb}
.fh{font-family:'Roboto Condensed',sans-serif;font-weight:700;font-size:12px;color:#ddd}
.flogo{font-family:'Roboto Condensed',sans-serif;font-weight:700;font-size:28px;color:#ddd}
.ftext{font-size:9.5px;line-height:19px;color:#aaa}
.fsocial{display:flex;gap:7px}
.fsocial span{width:22px;height:22px;border-radius:50%;background:#555;display:block}
.contact-row{width:182px;display:flex;align-items:center;gap:16px;font-size:10.5px;color:#bbb;padding-bottom:16px;border-bottom:1px solid #555}
.contact-row .ic{width:25px;height:25px;border-radius:50%;background:#4a4a4a;display:flex;align-items:center;justify-content:center}
.links{font-size:10px;line-height:22px;color:#aaa;list-style:none}
.baseline{left:0;top:2452px;width:1200px;height:73px;background:var(--base);color:#999;font-size:9.5px;display:flex;align-items:center;justify-content:center}
</style>
</head>
<body>

<header>
  <div class="abs hero" role="img" aria-label="Photo collage of an electrical switchboard, solar panels and a modern lit interior"></div>
  <div class="abs hero-shade"></div>
  <div class="abs social"><span></span><span></span><span></span></div>
  <div class="abs phone">
    <span class="ic"><svg width="12" height="12" viewBox="0 0 24 24"><path fill="#fff" d="M6.6 10.8a15.1 15.1 0 0 0 6.6 6.6l2.2-2.2c.3-.3.7-.4 1-.2 1.1.4 2.3.6 3.6.6.6 0 1 .4 1 1V20c0 .6-.4 1-1 1A17 17 0 0 1 3 4c0-.6.4-1 1-1h3.5c.6 0 1 .4 1 1 0 1.3.2 2.5.6 3.6.1.3 0 .7-.2 1z"/></svg></span>
    <span class="brand">TAVO</span> 139257
  </div>
  <nav class="abs nav">
    <div class="abs logo">Tavo</div>
    <div class="abs menu">
      <a class="active">HOME</a><a>TAVO STORY</a><a>OUR WORK</a><a>CONTACT US</a>
    </div>
  </nav>
  <h1 class="abs hero-title">ELECTRICAL<i>✣</i>LED LIGHTING<i>✣</i>SOLAR POWER</h1>
  <p class="abs hero-sub">AUSTRALIA'S LARGEST FULLY INTEGRATED ELECTRICAL &amp; ENERGY SOLUTIONS PROVIDER.</p>
  <div class="abs btn hero-btn">VIEW MORE
    <svg width="12" height="12" viewBox="0 0 12 12"><circle cx="6" cy="6" r="6" fill="#fff"/><path d="M5 3.5 7.5 6 5 8.5" stroke="#ec1f27" stroke-width="1.6" fill="none"/></svg>
  </div>
</header>

<section class="abs services"></section>
<div class="abs svc" style="left:200px;top:528px">
  <div class="circle"><svg width="56" height="56" viewBox="0 0 56 56" fill="none" stroke="#fff" stroke-width="4" stroke-linecap="round"><path d="M14 42 20 36"/><path d="M22 24l10 10-4 4a7 7 0 0 1-10-10z" fill="#fff"/><path d="M28 20l8 8M34 14l-6 6M42 22l-6 6"/><path d="M34 26l4-4a7 7 0 0 0-10-10l-4 4" fill="#fff"/></svg></div>
  ELECTRICAL
</div>
<div class="abs svc" style="left:501px;top:528px">
  <div class="circle"><svg width="56" height="56" viewBox="0 0 56 56" fill="#fff" stroke="#fff" stroke-width="3" stroke-linecap="round"><rect x="23" y="8" width="10" height="10" rx="2"/><path d="M18 18h20l4 14H14z"/><path d="M28 38v10M18 36l-5 8M38 36l5 8" fill="none"/></svg></div>
  LED LIGHTING
</div>
<div class="abs svc" style="left:800px;top:528px">
  <div class="circle"><svg width="58" height="58" viewBox="0 0 58 58" fill="none" stroke="#fff" stroke-width="3" stroke-linecap="round"><circle cx="29" cy="10" r="4" fill="#fff"/><path d="M29 2v-1M20 6l-2-2M38 6l2-2"/><rect x="10" y="18" width="38" height="24" rx="2"/><path d="M10 26h38M10 34h38M22 18v24M36 18v24M29 42v8M20 52h18"/></svg></div>
  SOLAR POWER
</div>

<section>
  <div class="abs about-frame"></div>
  <div class="abs about-photo" role="img" aria-label="Photo of hands stripping coloured electrical wires with pliers"></div>
  <h2 class="abs h2 about-h">ABOUT <b>TAVO</b></h2>
  <p class="abs about-p">Tavo Electrical was formed to be an expert Electricity Contracting Company providing services to all Residential and Commercial Customers. With over 10 years of experience, Tavo Electrical has developed a highly experienced team of professionals that ensure all our customer expectations are met.</p>
  <div class="abs btn about-btn">READ MORE</div>
</section>

<section>
  <div class="abs sec-head" style="top:1114px"><h2 class="h2">WHY CHOOSE <b>TAVO</b></h2><div class="rule"></div></div>

  <div class="abs reason" style="left:160px;top:1183px"><div class="abs num">1</div><h3>PROFESSIONAL SERVICE</h3><p>When you hire a Tavo Electrical Electrician you will get a professional and well-presented Electrician that comes skilled and ready to do the job.</p></div>
  <div class="abs reason" style="left:461px;top:1183px"><div class="abs num">2</div><h3>5 YEAR WORKMANSHIP GUARANTEE</h3><p>You can buy with confidence as all of our work has a 5 year workmanship guarantee. For your peace of mind, we unconditionally back our electrical work. We will come back to fix any problems at our own expense.</p></div>
  <div class="abs reason" style="left:761px;top:1183px"><div class="abs num">3</div><h3>VALUE FOR MONEY</h3><p>We provide extremely competitive pricing, which means you get value for money on quality that is comparable to the best in the industry.</p></div>
  <div class="abs reason" style="left:160px;top:1336px"><div class="abs num">4</div><h3>ENVIRONMENTALLY FRIENDLY</h3><p>We a committed to reducing carbon emissions by installing Solar Power and upgrading sites to LED Lighting. In addition to reducing the carbon emissions we recycle Fluorescent Tubes, Highbay Globes, Metal and Cardboard.</p></div>
  <div class="abs reason" style="left:461px;top:1336px"><div class="abs num">5</div><h3>FULLY INSURED</h3><p>Tavo Electrical is fully insured and equipped to handle break downs and service call outs.</p></div>
</section>

<section>
  <div class="abs sec-head" style="top:1546px"><h2 class="h2">CLIENT SPEAK FOR <b>TAVO</b></h2></div>
  <div class="abs testi"></div>
  <div class="abs avatar" role="img" aria-label="Client photo of a steel processing factory floor"></div>
  <div class="abs quote-mark">“</div>
  <p class="abs quote">Excellent work and very professional. Marcus takes time to explain everything and demonstrate workings. Very clear precise and accurate.</p>
  <p class="abs author">- DKELLS <em>GLENHAVEN EAST VIC</em></p>
  <div class="abs arrows">
    <span><svg width="8" height="10" viewBox="0 0 8 10"><path d="M6 1 2 5l4 4" stroke="#fff" stroke-width="1.6" fill="none"/></svg></span>
    <span><svg width="8" height="10" viewBox="0 0 8 10"><path d="M2 1l4 4-4 4" stroke="#fff" stroke-width="1.6" fill="none"/></svg></span>
  </div>
</section>

<section>
  <div class="abs sec-head" style="top:1955px"><h2 class="h2">OUR <b>CLIENTS</b></h2><div class="rule"></div></div>
  <div class="abs carr" style="left:162px"><svg width="6" height="8" viewBox="0 0 6 8"><path d="M5 1 1 4l4 3" stroke="#fff" stroke-width="1.4" fill="none"/></svg></div>
  <div class="abs client" style="left:212px;width:168px">Velvetrose</div>
  <div class="abs client" style="left:414px;width:165px">Outback Surplus</div>
  <div class="abs client" style="left:616px;width:167px">Heron Pipe Supplies</div>
  <div class="abs client" style="left:818px;width:167px">Goldcrest Burgers</div>
  <div class="abs carr" style="left:1019px"><svg width="6" height="8" viewBox="0 0 6 8"><path d="M1 1l4 3-4 3" stroke="#fff" stroke-width="1.4" fill="none"/></svg></div>
</section>

<footer>
  <div class="abs footer"></div>
  <div class="abs fh" style="left:162px;top:2198px">ABOUT US</div>
  <div class="abs flogo" style="left:162px;top:2228px">Tavo</div>
  <p class="abs ftext" style="left:162px;top:2284px;width:295px">Tavo Electrical was formed to be an expert Electricity Contracting Company providing services to all Residential and Commercial Customers. With over 10 years of experience, Tavo Electrical has developed a highly experienced team of professionals that ensure all our customer expectations are met.</p>
  <div class="abs fsocial" style="left:162px;top:2410px"><span></span><span></span><span></span></div>

  <div class="abs fh" style="left:539px;top:2198px">GET IN TOUCH</div>
  <div class="abs contact-row" style="left:539px;top:2240px"><span class="ic"><svg width="10" height="13" viewBox="0 0 10 13"><path d="M5 0a5 5 0 0 1 5 5c0 3.5-5 8-5 8S0 8.5 0 5a5 5 0 0 1 5-5z" fill="#ccc"/><circle cx="5" cy="5" r="1.8" fill="#4a4a4a"/></svg></span>dummy address, AU</div>
  <div class="abs contact-row" style="left:539px;top:2296px"><span class="ic"><svg width="11" height="11" viewBox="0 0 24 24"><path fill="#ccc" d="M6.6 10.8a15.1 15.1 0 0 0 6.6 6.6l2.2-2.2c.3-.3.7-.4 1-.2 1.1.4 2.3.6 3.6.6.6 0 1 .4 1 1V20c0 .6-.4 1-1 1A17 17 0 0 1 3 4c0-.6.4-1 1-1h3.5c.6 0 1 .4 1 1 0 1.3.2 2.5.6 3.6.1.3 0 .7-.2 1z"/></svg></span>139257</div>
  <div class="abs contact-row" style="left:539px;top:2352px;border-bottom:none"><span class="ic"><svg width="12" height="9" viewBox="0 0 12 9"><rect width="12" height="9" rx="1" fill="#ccc"/><path d="M0.5 0.8 6 5l5.5-4.2" stroke="#4a4a4a" fill="none"/></svg></span>info@tavoelectrical.com.au</div>

  <div class="abs fh" style="left:836px;top:2198px">QUICK LINKS</div>
  <ul class="abs links" style="left:836px;top:2232px">
    <li>Led Lighting</li><li>Solar Power</li><li>Electrical</li><li>Career</li><li>Terms and Conditions</li><li>Privacy</li>
  </ul>
  <div class="abs baseline">Copyright © 2017 tavoelectrical.com.au. All rights reserved.</div>
</footer>

</body>
</html>
```